24Std Betreuung Flyer Senioren
Zielgruppe
Wir vermitteln Ihnen Pflegekräfte aus Polen in 24h Betreuung. Zu diesem Zweck arbeiten wir mit unseren Partnerunternehmen in Polen und Litauen, welche ihre Pflegekraft im Rahmen der EU Dienstleistungsfreiheit legal nach Deutschland vermitteln. Das von uns vermittelte Personal ist freundlich und gut ausgebildet und verfügt über ausreichende bis gute Deutschkenntnisse. Unsere Agentur übernimmt die Koordinierung und Klärung aller Angelegenheiten für die An- und Abreise ihrer Pflegekraft. Das Personal wohnt mit der pflegebürftigen Person zusammen, wodurch wir eine 24h Betreuung realisieren können.
Aufgabenstellung
Seniorengerecht und nicht zu modern, übersichtlich nicht zu klein geschrieben evtl mit lizenzfreien Bildern von Senioren
Format: 6 seitig Wickelfalz
Informationen auf ww.altershilfe-plus.de

```html
<!DOCTYPE html>
<html lang="de">
<head>
<meta charset="utf-8">
<title>Altershilfe Plus – Flyer Wickelfalz</title>
<link rel="stylesheet" href="https://fonts.googleapis.com/css2?family=Arimo:ital,wght@0,400;0,700;1,700&display=swap">
<style>
  :root {
    --bg: #e4e4e4;
    --blue: #1e84c3;
    --blue-light: #48a4d6;
    --blue-dark: #0f5e9c;
    --ink: #1b5c9a;
    --grey: #7a7a7a;
    --paper: #f6f6f6;
    --photo-warm: #e9d9d2;
    --photo-green: #c9d8b6;
  }
  * { box-sizing: border-box; margin: 0; padding: 0; }
  html, body { width: 1200px; height: 960px; overflow: hidden; }
  body {
    background: var(--bg);
    font-family: "Arimo", Arial, sans-serif;
    position: relative;
  }
  .sheet {
    position: absolute;
    left: 270px;
    width: 660px;
    height: 440px;
    display: grid;
    grid-template-columns: repeat(3, 220px);
    background: var(--paper);
    box-shadow: 0 6px 18px rgba(0,0,0,.18);
  }
  .sheet--outside { top: 28px; }
  .sheet--inside { top: 492px; grid-template-columns: 220px 440px; }
  .panel { display: flex; flex-direction: column; overflow: hidden; position: relative; }
  .panel + .panel { border-left: 1px solid rgba(0,0,0,.06); }

  .blue-block {
    background: linear-gradient(160deg, var(--blue-light), var(--blue) 60%, var(--blue-dark));
    color: #fff;
    padding: 18px 14px;
  }
  .services { flex: none; }
  .services--outer { min-height: 178px; padding-bottom: 16px; }
  .services--inner { min-height: 226px; }
  .services h2 { font-size: 11px; font-weight: 700; margin-bottom: 6px; }
  .ticks { list-style: none; }
  .ticks li {
    font-size: 9px; line-height: 1.45; padding-left: 12px; position: relative;
  }
  .ticks li svg { position: absolute; left: 0; top: 4px; width: 7px; height: 7px; }

  .stripes { height: 14px; flex: none; display: flex; flex-direction: column; justify-content: space-between; padding: 2px 0; }
  .stripes span { display: block; height: 3px; background: var(--blue); }
  .stripes span:nth-child(2) { background: var(--blue-light); }

  .photo { flex: 1; min-height: 0; }
  .photo--cane-woman { background: linear-gradient(135deg, #ddd4cf, var(--photo-warm) 50%, #f4ece8); }
  .photo--walker { background: linear-gradient(120deg, #d7e4e6, #efe7e1 60%, #e2d3c9); height: 118px; flex: none; }
  .photo--cane-hands { background: linear-gradient(160deg, #e3e8d6, var(--photo-green) 50%, #eadcd3); }
  .photo--group { background: linear-gradient(120deg, #6c9a62, #d9a89a 40%, #c9d6e6 70%, #e9c8c0); height: 226px; flex: none; }

  .quote { flex: none; height: 128px; padding: 20px 18px 0; text-align: center; }
  .quote p { font-size: 11px; font-weight: 700; font-style: italic; color: var(--ink); line-height: 1.35; }
  .quote cite { display: block; margin-top: 8px; font-style: normal; font-size: 8px; letter-spacing: 3px; color: var(--grey); }

  .contact { flex: 1; text-align: center; font-size: 9.5px; line-height: 1.55; padding-top: 22px; }
  .contact strong { display: block; font-size: 11px; margin-bottom: 2px; }

  .brand { height: 150px; display: flex; align-items: center; justify-content: center; gap: 8px; flex: none; }
  .brand__dot { width: 22px; height: 22px; border-radius: 50%; background: var(--blue); }
  .brand__name { font-size: 21px; font-weight: 400; color: var(--ink); }

  .tagline { flex: none; background: #ecefef; padding: 12px 16px; text-align: center; color: var(--ink); }
  .tagline span { display: block; font-size: 13px; }
  .tagline strong { display: block; font-size: 19px; font-weight: 700; }

  .care { flex: 1; padding: 14px 30px 0; color: var(--ink); }
  .care h2 { font-size: 11px; font-weight: 700; margin-bottom: 10px; }
  .care .ticks li { font-size: 10.5px; line-height: 1.65; padding-left: 14px; }
  .care .ticks li svg { top: 5px; }
  .spacer { flex: 1; }
</style>
</head>
<body>
  <svg width="0" height="0" style="position:absolute">
    <symbol id="tick" viewBox="0 0 10 10"><path d="M1 5.5 L4 8.5 L9 1.5" fill="none" stroke="currentColor" stroke-width="2"/></symbol>
  </svg>

  <section class="sheet sheet--outside">
    <div class="panel">
      <div class="blue-block services services--outer">
        <h2>Unsere Dienstleistungen</h2>
        <ul class="ticks">
          <li><svg><use href="#tick"/></svg>legales Pflegepersonal (A1-Bescheinigung)</li>
          <li><svg><use href="#tick"/></svg>bezahlbare Alternative zum Pflegeheim</li>
          <li><svg><use href="#tick"/></svg>mehrere Kooperationspartner aus Osteuropa</li>
          <li><svg><use href="#tick"/></svg>deutschsprachige Betreuer/ innen</li>
          <li><svg><use href="#tick"/></svg>langjährige Erfahrung</li>
          <li><svg><use href="#tick"/></svg>kostenfreier Besichtigungstermin</li>
          <li><svg><use href="#tick"/></svg>zielgerichtete Beratung vor Ort</li>
          <li><svg><use href="#tick"/></svg>individuelles und unverbindliches Angebot</li>
          <li><svg><use href="#tick"/></svg>Koordination und Organisation der gesamten Auftragsabwicklung</li>
        </ul>
      </div>
      <div class="stripes"><span></span><span></span><span></span></div>
      <div class="photo photo--cane-woman" role="img" aria-label="Foto: lächelnde Seniorin mit Gehstock, eine Hand auf ihrer Schulter"></div>
    </div>

    <div class="panel">
      <div class="photo photo--walker" role="img" aria-label="Foto: Pflegekraft stützt die Hände eines Menschen am Rollator"></div>
      <div class="stripes"><span></span><span></span><span></span></div>
      <blockquote class="quote">
        <p>„Es geht nicht darum, dem Leben mehr Tage zu geben, sondern den Tagen mehr Leben zu geben.“</p>
        <cite>MARTA SEIDEL</cite>
      </blockquote>
      <div class="stripes"><span></span><span></span><span></span></div>
      <div class="blue-block contact">
        <strong>Altershilfe Plus</strong>
        Geschäftsführer: Jens Karwitz<br>
        www.altershilfe-plus.de<br>
        Email: j.karwitz@altershilfe-plus.de<br>
        Tel. 0176 000 45 678<br>
        Festnetz: 02428 000119<br>
        Fax: 02428 000120
      </div>
    </div>

    <div class="panel">
      <div class="brand">
        <span class="brand__dot"></span>
        <span class="brand__name">Altershilfe Plus</span>
      </div>
      <div class="stripes"><span></span><span></span><span></span></div>
      <div class="tagline">
        <span>Wir kümmern uns um</span>
        <strong>Ihre Bedürfnisse</strong>
      </div>
      <div class="photo photo--cane-hands" role="img" aria-label="Foto: zwei Hände übereinander auf einem hölzernen Gehstock"></div>
    </div>
  </section>

  <section class="sheet sheet--inside">
    <div class="panel">
      <div class="blue-block services services--inner">
        <h2>Unsere Dienstleistungen</h2>
        <ul class="ticks">
          <li><svg><use href="#tick"/></svg>legales Pflegepersonal (A1-Bescheinigung)</li>
          <li><svg><use href="#tick"/></svg>bezahlbare Alternative zum Pflegeheim</li>
          <li><svg><use href="#tick"/></svg>mehrere Kooperationspartner aus Osteuropa</li>
          <li><svg><use href="#tick"/></svg>deutschsprachige Betreuer/ innen</li>
          <li><svg><use href="#tick"/></svg>langjährige Erfahrung</li>
          <li><svg><use href="#tick"/></svg>kostenfreier Besichtigungstermin</li>
          <li><svg><use href="#tick"/></svg>zielgerichtete Beratung vor Ort</li>
          <li><svg><use href="#tick"/></svg>individuelles und unverbindliches Angebot</li>
        </ul>
      </div>
      <div class="stripes"><span></span><span></span><span></span></div>
      <div class="spacer"></div>
      <div class="stripes"><span></span><span></span><span></span></div>
    </div>

    <div class="panel">
      <div class="photo photo--group" role="img" aria-label="Foto: vier Senioren sitzen gemeinsam im Garten am Tisch und schauen auf ein Smartphone"></div>
      <div class="stripes"><span></span><span></span><span></span></div>
      <div class="care">
        <h2>Wir kümmern uns um Sie</h2>
        <ul class="ticks">
          <li><svg><use href="#tick"/></svg>Schwierigkeit der Betreuung ist nicht zwingend abhängig vom Pflegegrad</li>
          <li><svg><use href="#tick"/></svg>Anforderung an die Betreuerin (Sprachkenntnisse, Pflege-Erfahrungen...)</li>
          <li><svg><use href="#tick"/></svg>Anzahl der im Haushalt zu pflegenden Personen</li>
          <li><svg><use href="#tick"/></svg>Anzahl von nächtlichen Einsätzen</li>
        </ul>
      </div>
      <div class="stripes"><span></span><span></span><span></span></div>
    </div>
  </section>
</body>
</html>
```